Venture Capital Firm Needs Website Redesign

We need a bold revamp of our website (https://halvenmoor.vc/)
which at the moment looks washed out. We want a crisp, fresh and unique look. Feel free to keep as much or as little content in the site. The only thing we need to keep is a team section. The site should convey a clear distinction between our 3 product lines: Venture Capital, Private Credit, and Crypto. Two versions of our logo are attached and they should not change. For design inspirations, we like http://www.plumridgecap.com/ for a more simple site and for a more built out site we like http://tallowgate.com/

Updates
Industry/Entity Type
Investment
Coding
Coded - Design and coding required
Number of Pages Required
1 page
Font styles to use
Colors
Designer to choose colors to be used in the design.
Requirements
Must have
- - Clear distinction between our 3 product lines: Venture Capital, Private Credit
- - Team section

Nice to have
- Some really creative aspect like http://www.plumridgecap.com/ has with the distinction between first, second, and third kind

```html
<!DOCTYPE html>
<html lang="en">
<head>
<meta charset="utf-8">
<title>Halvenmoor</title>
<link rel="stylesheet" href="https://fonts.googleapis.com/css2?family=Montserrat:wght@400;600;700&family=Open+Sans:wght@400;600&display=swap">
<style>
:root{
  --green:#8cb21f;
  --ink:#2b2b2b;
  --muted:#666;
  --bg-1:#ffffff;
  --bg-2:#f3f3f3;
  --bg-3:#e9e9e9;
  --bg-4:#d8d8d8;
  --bg-5:#0c0c0c;
  --line:#cfcfcf;
}
*{box-sizing:border-box;margin:0;padding:0}
html,body{width:1200px;height:3364px;overflow:hidden}
body{font-family:"Open Sans",Arial,sans-serif;color:var(--ink)}
.panel{position:relative;width:1200px;overflow:hidden}
.panel--venture{height:672px;background:var(--bg-1)}
.panel--credit{height:672px;background:var(--bg-2)}
.panel--crypto{height:672px;background:var(--bg-3)}
.panel--team{height:676px;background:var(--bg-4)}
.panel--contact{height:672px;background:var(--bg-5);color:#fff}
.brand{position:absolute;left:160px;top:22px;font-family:"Montserrat",sans-serif;font-weight:600;font-size:34px;letter-spacing:1px;color:var(--ink)}
.panel--contact .brand{color:#fff}
.nav{position:absolute;left:590px;top:36px;display:flex;gap:32px;font-family:"Montserrat",sans-serif;font-size:11px;font-weight:600;color:#444}
.panel--contact .nav{color:#ddd}
.nav .is-active{color:var(--green)}
.social{position:absolute;left:164px;top:98px;display:flex;flex-direction:column;gap:9px}
.social span{width:26px;height:26px;border:2px solid var(--ink);border-radius:50%;display:block}
.panel--contact .social span{border-color:#fff}
.title{position:absolute;left:0;width:1200px;text-align:center;font-family:"Montserrat",sans-serif;font-weight:700;font-size:36px;letter-spacing:1px}
.copy{position:absolute;left:330px;width:540px;text-align:center;font-size:10.5px;line-height:17px;color:var(--muted)}
.badges{position:absolute;left:0;width:1200px;display:flex;justify-content:center;gap:22px}
.badge{width:125px;height:64px;border:2px solid #333;background:#fff;display:flex;align-items:center;justify-content:center;font-family:"Montserrat",sans-serif;font-weight:600;font-size:15px;color:#333}
.pager{position:absolute;left:1148px;top:325px;display:flex;flex-direction:column;gap:8px}
.pager span{width:8px;height:8px;border-radius:50%;background:#bbb}
.pager span:first-child{background:#555}
.mouse{position:absolute;left:586px;top:588px;width:26px;height:42px;border:2px solid #333;border-radius:13px}
.mouse::after{content:"";position:absolute;left:10px;top:8px;width:2px;height:8px;background:#333}
.btn{position:absolute;border:2px solid #333;font-family:"Montserrat",sans-serif;font-weight:600;font-size:11px;letter-spacing:1px;display:flex;align-items:center;justify-content:center}
.subtitle{position:absolute;left:0;width:1200px;text-align:center;font-family:"Montserrat",sans-serif;font-weight:600;font-size:12px;color:var(--green)}
.member{position:absolute;top:275px;width:230px}
.member__photo{width:230px;height:270px;border:8px solid #fff;background:linear-gradient(160deg,#9a9a9a,#4a4a4a)}
.member__name{margin-top:16px;font-family:"Montserrat",sans-serif;font-weight:700;font-size:13px}
.member__role{margin-top:6px;font-size:10px;line-height:15px;color:#555}
.arrow{position:absolute;top:398px;width:28px;height:28px;border:2px solid #333;border-radius:50%}
.field{position:absolute;top:240px;width:200px;height:34px;background:#fff}
.info{position:absolute;top:414px;left:0;width:1200px;display:flex;justify-content:center;gap:70px;font-size:11px;color:#ddd;align-items:center}
.info span{display:flex;align-items:center;gap:8px}
.partners{position:absolute;top:474px;left:0;width:1200px;display:flex;justify-content:center;gap:48px;font-family:"Montserrat",sans-serif;font-weight:600;font-size:16px;color:#fff}
.legal{position:absolute;top:598px;left:0;width:1200px;text-align:center;font-size:10px;color:#aaa}
</style>
</head>
<body>

<section class="panel panel--venture">
  <div class="brand">HALVENMOOR</div>
  <nav class="nav"><span class="is-active">VENTURE</span><span>PRIVATE CREDIT</span><span>CRYPTO</span><span>ABOUT US</span><span>TEAM</span><span>BLOG</span></nav>
  <div class="social"><span></span><span></span><span></span><span></span></div>
  <h1 class="title" style="top:212px">VENTURE CAPITAL</h1>
  <p class="copy" style="top:272px">We invest in early-stage and growth companies led by founders with rare conviction. Our team backs businesses that reshape their markets, and we stay close from the first cheque onward, helping with hiring, strategy and follow-on capital. Below are a few of the companies we are proud to support.</p>
  <div class="badges" style="top:405px">
    <div class="badge">Tallyhop</div><div class="badge">Meridale</div><div class="badge">Parcelle</div><div class="badge">Loomwell</div>
  </div>
  <div class="pager"><span></span><span></span><span></span><span></span></div>
  <div class="mouse"></div>
</section>

<section class="panel panel--credit">
  <div class="brand">HALVENMOOR</div>
  <nav class="nav"><span>VENTURE</span><span class="is-active">PRIVATE CREDIT</span><span>CRYPTO</span><span>ABOUT US</span><span>TEAM</span><span>BLOG</span></nav>
  <div class="social"><span></span><span></span><span></span><span></span></div>
  <h2 class="title" style="top:210px">PRIVATE CREDIT</h2>
  <p class="copy" style="top:268px">Halvenmoor Private Credit provides capital to lending businesses that use technology to reach borrowers overlooked by traditional banks. We structure facilities that grow with our partners, pairing disciplined underwriting with a deep understanding of data-driven credit models and the teams that build them.</p>
  <div class="badges" style="top:400px">
    <div class="badge" style="width:120px;height:74px">Greenrow</div><div class="badge" style="width:120px;height:74px">Brookfin</div><div class="badge" style="width:180px;height:74px">Lumenledger</div>
  </div>
</section>

<section class="panel panel--crypto">
  <div class="brand">HALVENMOOR</div>
  <nav class="nav"><span>VENTURE</span><span>PRIVATE CREDIT</span><span class="is-active">CRYPTO</span><span>ABOUT US</span><span>TEAM</span><span>BLOG</span></nav>
  <div class="social"><span></span><span></span><span></span><span></span></div>
  <h2 class="title" style="top:226px">CRYPTO</h2>
  <p class="copy" style="top:286px">The Halvenmoor Crypto Fund offers investors exposure to a diversified basket of digital assets, managed with the same rigour we bring to every strategy. Our research team tracks market structure, custody and liquidity so that investors can participate with confidence.</p>
  <div class="btn" style="left:532px;top:406px;width:134px;height:40px">READ MORE</div>
</section>

<section class="panel panel--team">
  <div class="brand">HALVENMOOR</div>
  <nav class="nav"><span>VENTURE</span><span>PRIVATE CREDIT</span><span>CRYPTO</span><span>ABOUT US</span><span class="is-active">TEAM</span><span>BLOG</span></nav>
  <div class="social"><span></span><span></span><span></span><span></span></div>
  <h2 class="title" style="top:172px">OUR TEAM</h2>
  <p class="subtitle" style="top:218px">The people behind the firm</p>
  <div class="arrow" style="left:150px"></div>
  <div class="member" style="left:205px">
    <div class="member__photo" role="img" aria-label="Portrait photo of Amir Hadley"></div>
    <div class="member__name">AMIR HADLEY</div>
    <div class="member__role">Managing Partner and co-founder, leading venture and credit strategy for the firm.</div>
  </div>
  <div class="member" style="left:485px">
    <div class="member__photo" role="img" aria-label="Portrait photo of Niran Rao"></div>
    <div class="member__name">NIRAN RAO</div>
    <div class="member__role">Partner focused on private credit, sourcing and structuring lending facilities worldwide.</div>
  </div>
  <div class="member" style="left:765px">
    <div class="member__photo" role="img" aria-label="Portrait photo of Jalen Sommers"></div>
    <div class="member__name">JALEN SOMMERS</div>
    <div class="member__role">Partner overseeing the crypto fund, research and digital asset operations.</div>
  </div>
  <div class="arrow" style="left:1010px"></div>
</section>

<section class="panel panel--contact">
  <div class="brand">HALVENMOOR</div>
  <nav class="nav"><span>VENTURE</span><span>PRIVATE CREDIT</span><span>CRYPTO</span><span>ABOUT US</span><span>TEAM</span><span>BLOG</span></nav>
  <div class="social"><span></span><span></span><span></span><span></span></div>
  <h2 class="title" style="top:192px">CONTACT US</h2>
  <div class="field" style="left:398px"></div>
  <div class="field" style="left:604px"></div>
  <div class="btn" style="left:398px;top:284px;width:406px;height:30px;border-color:#fff;color:#fff">GROW MY BUSINESS</div>
  <div class="info">
    <span><svg width="12" height="16" viewBox="0 0 12 16"><path d="M6 0a6 6 0 0 0-6 6c0 4.5 6 10 6 10s6-5.5 6-10a6 6 0 0 0-6-6zm0 8.5A2.5 2.5 0 1 1 6 3.5a2.5 2.5 0 0 1 0 5z" fill="#fff"/></svg>48 Larkin Street, Suite 210, Portland</span>
    <span><svg width="16" height="12" viewBox="0 0 16 12"><rect x="0.5" y="0.5" width="15" height="11" fill="none" stroke="#fff"/><path d="M1 1l7 6 7-6" fill="none" stroke="#fff"/></svg>hello@halvenmoor.vc</span>
    <span><svg width="14" height="14" viewBox="0 0 14 14"><path d="M3 0l3 3-2 2c1 2 3 4 5 5l2-2 3 3-2 3C6 14 0 8 0 3z" fill="#fff"/></svg>(503) 555-0148</span>
  </div>
  <div class="partners"><span>Orrin</span><span>Tamsin</span><span>Northvale</span><span>Kestrel</span><span>Verity</span><span>Wexmoor</span></div>
  <p class="legal">Copyright © 2020. Halvenmoor. All Rights Reserved.</p>
</section>

</body>
</html>
```